Stationary Package for New Bookkeeping Business

We need the following stationary designs:

- Business Card
- Letterhead
- With Comps
- Envelopes
- Paper Folder
- Email Signature

We will provide accounting and bookkeeping services to small business. We would like have the main color as blue and have a modern professional look.

Variations of colour and shades of blue welcome
Preference for deeper darker blue - navy

Variations of font in logo also welcome

Requirements
Must have
• Rosalind
B.Bus (Accounting)
Registered BAS Agent

Phone 0491 382 507
Post PO Box 947 Kelmora NSW 2768

Email rosalind@tarwinledgers.com

Business Card to be bold and eye catching

Should not have
• Letter head to not have too much colour on it

```html
<!DOCTYPE html>
<html lang="en">
<head>
<meta charset="utf-8">
<title>Tarwin Ledgers — Letterhead</title>
<link rel="stylesheet" href="https://fonts.googleapis.com/css2?family=Questrial&display=swap">
<style>
  :root {
    --backdrop: #d9d9d9;
    --paper: #f4f4f4;
    --navy: #10305f;
    --teal: #2f7392;
    --ink-soft: #4a4f57;
  }
  * { box-sizing: border-box; margin: 0; padding: 0; }
  html, body {
    width: 1200px;
    height: 968px;
    overflow: hidden;
    background: var(--backdrop);
    font-family: "Questrial", "Century Gothic", sans-serif;
  }
  .canvas {
    position: relative;
    width: 1200px;
    height: 968px;
  }
  .letterhead {
    position: absolute;
    left: 282px;
    top: 34px;
    width: 636px;
    height: 900px;
    background: var(--paper);
    box-shadow: 0 2px 10px rgba(0,0,0,0.12);
  }
  .brand {
    position: absolute;
    left: 52px;
    top: 54px;
    display: flex;
    align-items: center;
    gap: 10px;
  }
  .brand-square {
    width: 38px;
    height: 38px;
    background: var(--navy);
  }
  .brand-name {
    color: var(--navy);
    font-size: 22px;
    line-height: 1.02;
  }
  .contact {
    position: absolute;
    left: 52px;
    bottom: 104px;
    color: var(--ink-soft);
    font-size: 9.5px;
    line-height: 1.6;
  }
  .contact-row {
    display: flex;
    gap: 18px;
  }
  .contact-item {
    display: inline-flex;
    align-items: center;
    gap: 4px;
  }
  .contact-item svg { width: 9px; height: 9px; }
  .rule-navy {
    position: absolute;
    left: 52px;
    bottom: 88px;
    width: 368px;
    height: 4px;
    background: var(--navy);
  }
  .rule-teal {
    position: absolute;
    left: 428px;
    bottom: 82px;
    width: 130px;
    height: 4px;
    background: var(--teal);
  }
  .website {
    position: absolute;
    right: 78px;
    bottom: 96px;
    color: var(--ink-soft);
    font-size: 10px;
  }
  .website strong { color: var(--navy); font-weight: 400; }
</style>
</head>
<body>
<div class="canvas">
  <section class="letterhead">
    <header class="brand">
      <span class="brand-square"></span>
      <span class="brand-name">Tarwin<br>Ledgers</span>
    </header>

    <footer>
      <div class="contact">
        <div class="contact-address">PO Box 947 Kelmora NSW 2768</div>
        <div class="contact-row">
          <span class="contact-item">
            <svg viewBox="0 0 10 10"><circle cx="5" cy="5" r="4.5" fill="none" stroke="currentColor" stroke-width="0.8"/><path d="M3.3 2.6l1 1-0.6 0.6c0.4 0.8 1 1.4 1.8 1.8l0.6-0.6 1 1-0.8 0.9C4.7 7 3 5.3 2.7 3.4z" fill="currentColor"/></svg>
            0491 382 507
          </span>
          <span class="contact-item">
            <svg viewBox="0 0 10 10"><circle cx="5" cy="5" r="4.5" fill="none" stroke="currentColor" stroke-width="0.8"/><rect x="3" y="4" width="4" height="2.6" fill="currentColor"/><rect x="3.6" y="2.6" width="2.8" height="1.2" fill="currentColor"/></svg>
            0491 382 507
          </span>
          <span class="contact-item">
            <svg viewBox="0 0 10 10"><circle cx="5" cy="5" r="4.5" fill="none" stroke="currentColor" stroke-width="0.8"/><rect x="2.8" y="3.3" width="4.4" height="3.2" fill="none" stroke="currentColor" stroke-width="0.7"/><path d="M2.8 3.3L5 5.1 7.2 3.3" fill="none" stroke="currentColor" stroke-width="0.7"/></svg>
            rosalind@tarwinledgers.com
          </span>
        </div>
      </div>
      <div class="rule-navy"></div>
      <div class="website">www.<strong>tarwinledgers</strong>.com</div>
      <div class="rule-teal"></div>
    </footer>
  </section>
</div>
</body>
</html>
```